KVR Biz Cards

We are a property management company that manages luxury level residential estates. As such, we need a business card design that gives a high end feel. The idea at the moment is to list the services offered on the back of the card, and our company information on the front of the card.

Services for the back of the card are as follows:
Professional Property Management service, Home Hosting & Concierge Service, Holliday Home / Income Property Management

```html
<!DOCTYPE html>
<html lang="en">
<head>
<meta charset="utf-8">
<title>KVR Management Business Card</title>
<link href="https://fonts.googleapis.com/css2?family=Playfair+Display:wght@700&family=Open+Sans:wght@400;600;700&display=swap" rel="stylesheet">
<style>
  :root {
    --bronze: #8a5a2b;
    --ink: #1a1a1a;
    --paper: #ffffff;
    --stage: #ffffff;
    --ribbon: #0d0d0d;
    --edge: #cfcfcf;
  }
  * { box-sizing: border-box; margin: 0; padding: 0; }
  html, body { width: 1200px; height: 360px; overflow: hidden; background: var(--stage); }
  .canvas { position: relative; width: 1200px; height: 360px; font-family: "Open Sans", Arial, sans-serif; color: var(--ink); }

  .card { position: absolute; top: 28px; height: 286px; background: var(--paper); border: 1px solid var(--edge); }
  .card--front { left: 66px; width: 500px; }
  .card--back { left: 604px; width: 541px; }

  .trim { position: absolute; background: var(--bronze); }

  .card--front .trim-top { left: -1px; top: -1px; width: 390px; height: 6px; }
  .card--front .trim-left { left: -1px; top: -1px; width: 6px; height: 200px; }
  .card--front .trim-corner-h { right: -8px; bottom: -8px; width: 60px; height: 8px; }
  .card--front .trim-corner-v { right: -8px; bottom: -8px; width: 8px; height: 240px; }

  .card--back .trim-top { left: -1px; top: -1px; width: 390px; height: 6px; }
  .card--back .trim-left { left: -1px; top: -1px; width: 6px; height: 286px; }
  .card--back .trim-corner-h { right: -8px; bottom: -8px; width: 60px; height: 8px; }
  .card--back .trim-corner-v { right: -8px; bottom: -8px; width: 8px; height: 200px; }

  .holder-name { position: absolute; left: 34px; top: 34px; font-family: "Playfair Display", Georgia, serif; font-weight: 700; font-size: 31px; color: var(--bronze); letter-spacing: 0.3px; }
  .holder-title { position: absolute; left: 34px; top: 78px; font-size: 20px; color: #333; }

  .brand { position: absolute; text-align: center; }
  .brand-name { font-weight: 700; color: var(--ink); letter-spacing: 0.6px; white-space: nowrap; }
  .brand-tagline { color: var(--bronze); white-space: nowrap; }

  .card--front .brand { left: 236px; top: 134px; width: 232px; }
  .card--front .brand-name { font-size: 17px; line-height: 22px; }
  .card--front .brand-tagline { font-size: 11.5px; line-height: 16px; }

  .card--back .brand { left: 170px; top: 90px; width: 200px; }
  .card--back .brand-name { font-size: 11px; line-height: 15px; }
  .card--back .brand-tagline { font-size: 8px; line-height: 11px; }

  .contact-list { position: absolute; left: 34px; top: 190px; list-style: none; }
  .contact-item { display: flex; align-items: center; gap: 10px; font-size: 20px; line-height: 28px; color: #222; }
  .contact-icon { width: 12px; height: 12px; border-top: 2px solid var(--bronze); border-left: 2px solid var(--bronze); border-bottom: 2px solid var(--bronze); }

  .service-list { position: absolute; left: 64px; top: 141px; list-style: none; }
  .service { width: 414px; height: 28px; margin-bottom: 21px; display: flex; align-items: center; justify-content: center; background: var(--ribbon); color: #fff; font-size: 14.5px; clip-path: polygon(0 0, 100% 0, 97% 50%, 100% 100%, 0 100%, 3% 50%); }
</style>
</head>
<body>
<div class="canvas">
  <section class="card card--front" aria-label="Front of business card">
    <span class="trim trim-top"></span><span class="trim trim-left"></span>
    <span class="trim trim-corner-h"></span><span class="trim trim-corner-v"></span>

    <h1 class="holder-name">Your Name</h1>
    <p class="holder-title">Your Title</p>

    <div class="brand">
      <p class="brand-name">KVR MANAGEMENT</p>
      <p class="brand-tagline">Crafted to Keep Your Estate at Ease</p>
    </div>

    <ul class="contact-list">
      <li class="contact-item"><span class="contact-icon"></span>(555) XXX XXX</li>
      <li class="contact-item"><span class="contact-icon"></span>yourmailid@mailbox.com</li>
      <li class="contact-item"><span class="contact-icon"></span>www.kvr.com</li>
    </ul>
  </section>

  <section class="card card--back" aria-label="Back of business card">
    <span class="trim trim-top"></span><span class="trim trim-left"></span>
    <span class="trim trim-corner-h"></span><span class="trim trim-corner-v"></span>

    <div class="brand">
      <p class="brand-name">KVR MANAGEMENT</p>
      <p class="brand-tagline">Crafted to Keep Your Estate at Ease</p>
    </div>

    <ul class="service-list">
      <li class="service">Professional Property Management service</li>
      <li class="service">Home Hosting &amp; Concierge Service</li>
      <li class="service">Holliday Home / Income Property Management</li>
    </ul>
  </section>
</div>
</body>
</html>
```